Photoshop Design Project

Just looking to use some existing element in emails and printed flyers for a lunch menu promo.

I am attaching a menu in progress to reference only the front page design of a chalkboard, chalk fonts, tagline of :Break from the Status Quo for Lunch On The GO. Its on the front of the menu.

I just want to drop in a photo of each on three separate pieces with description.

THe design should not be a match to the front of the menu, just utilize its elements. the design is not a lead at all, these should remain familiar with the front of the menu, but please use the elements to your design preference.

Ok to submit one layout that we can repeat, or ok to submit three different versions

Must stick with the colors though, they are brand color combo, not exact by color code, but the oranges and the browns need to stay somewhere and in some capacity.
SO menu attached, check out the front cover for inspirations, to go in email sends embedded, and to print as a flyer.

There are also three images attached they are the to be dropped into each piece, with a desciption
Updates

Project Deadline Extended
Reason: seems to be too many questions and I wasnt getting anywhere.. To clarify...One Design Piece (one page), three separate items, same peice, however three total. one for each product photo supplied

I moved the deadline back as there were many questions. To clarify, one design piece to be reused for three different products (sandwiches in this case) Same piece, but one for each sandwich.

I posted a file called Artmarket that now has each photo partnered with its title and description

Target Market(s)

hungry people looking for lunch

Industry/Entity Type

Promo

Requirements
Must have
• Attached Menu front page elements, of chalkboard, chalk font existing front colors.

```html
<!DOCTYPE html>
<html lang="en">
<head>
<meta charset="utf-8">
<title>Steak Sandwich – Lunch Menu Promo</title>
<link rel="stylesheet" href="https://fonts.googleapis.com/css2?family=Covered+By+Your+Grace&family=Libre+Baskerville:wght@700&display=swap">
<style>
  :root {
    --board-light: #3b3b3b;
    --board-mid: #262626;
    --board-dark: #161616;
    --frame: #fbfbf8;
    --orange: #f26a1b;
    --orange-text: #f47a2a;
    --chalk: #ffffff;
    --label-bg: rgba(58, 58, 58, 0.92);
    --caption-bg: rgba(18, 14, 12, 0.86);
  }
  * { margin: 0; padding: 0; box-sizing: border-box; }
  html, body { width: 1200px; height: 1200px; overflow: hidden; }
  body {
    position: relative;
    background: radial-gradient(ellipse at 50% 45%, var(--board-light) 0%, var(--board-mid) 55%, var(--board-dark) 100%);
    font-family: "Libre Baskerville", Georgia, serif;
  }
  .promo-frame {
    position: absolute;
    left: 102px; top: 97px;
    width: 996px; height: 998px;
    background: var(--frame);
    box-shadow: 0 6px 22px rgba(0, 0, 0, 0.55);
  }
  .dish-photo {
    position: absolute;
    left: 160px; top: 157px;
    width: 880px; height: 880px;
    background: linear-gradient(180deg,
      #e9dccb 0%, #d9b98c 18%, #b07a45 30%,
      #7a3a2c 42%, #b4574f 55%, #6f3a2a 68%,
      #4f6b2e 80%, #8a5a3c 90%, #3b2418 100%);
  }
  .menu-tag {
    position: absolute;
    left: 72px; top: 224px;
    width: 258px; height: 150px;
    background: var(--label-bg);
    border: 2px solid rgba(255, 255, 255, 0.35);
    box-shadow: 0 4px 12px rgba(0, 0, 0, 0.5);
    text-align: center;
    font-family: "Libre Baskerville", Georgia, serif;
    font-weight: 700;
    color: var(--chalk);
  }
  .menu-tag__title {
    font-size: 44px;
    letter-spacing: 10px;
    line-height: 1;
    margin-top: 26px;
    padding-left: 10px;
  }
  .menu-tag__brand {
    font-size: 24px;
    line-height: 1;
    margin-top: 18px;
  }
  .dish-title {
    position: absolute;
    left: 630px; top: 420px;
    width: 522px; height: 185px;
    background: var(--orange);
    box-shadow: 0 4px 12px rgba(0, 0, 0, 0.45);
    padding: 16px 0 0 18px;
    font-family: "Covered By Your Grace", cursive;
    font-weight: 400;
    font-size: 34px;
    line-height: 39px;
    letter-spacing: 1.5px;
    text-transform: uppercase;
    white-space: nowrap;
    color: var(--chalk);
  }
  .dish-caption {
    position: absolute;
    left: 43px; top: 793px;
    width: 521px; height: 127px;
    background: var(--caption-bg);
    padding: 14px 0 0 127px;
    font-weight: 700;
    font-size: 24px;
    line-height: 34px;
    white-space: nowrap;
    color: var(--chalk);
  }
  .dish-caption__highlight { color: var(--orange-text); }
</style>
</head>
<body>
  <div class="promo-frame"></div>
  <div class="dish-photo" role="img" aria-label="Photo of a sliced steak sandwich on floured ciabatta with blue cheese and watercress"></div>

  <div class="menu-tag">
    <div class="menu-tag__title">MENU</div>
    <div class="menu-tag__brand">Midday Bistro</div>
  </div>

  <h1 class="dish-title">Steak sandwich with<br>blue cheese, roasted<br>garlic mayonnaise and<br>balsamic vinegar reduction</h1>

  <p class="dish-caption">Topped with <span class="dish-caption__highlight">Roquefort</span><br><span class="dish-caption__highlight">Cheese</span> and watercress on<br>Fresh Ciabatta Bread</p>
</body>
</html>
```